Fahnendesign für Lenk & Stabe Elektrotechnik
Zielgruppe
Lenk & Stabe Elektrotechnik hat sich spezialisiert auf die Errichtung elektrischer Anlagen im Wohn-Neubau und bei Sanierungen von Wohnungen und Einfamilienhäusern. Unsere Zielgruppe sind Bauunternehmen und private Bauherren.
Aufgabenstellung
-Design nach Vorgaben Druckfalter ( Befestigung links )
Natürlich soll unser Logo gut zu sehen sein sowie unsere Internetseite : www.lenk-stabe.de
Firmenschriftart: Titel Fira Sans , Schrift : Montserrat
Vielleicht kann ein Bezug auf die Positionierung hergestellt werden , ist aber kein muss.
Alles andere kann kreativ entschieden werden. Schaut gerne auf unsere Social Media Kanäle:
https://www.instagram.example/lenk_stabe_elektrotechnik/?hl=de
https://www.facebook.example/lenkstabeelektrotechnik/

```html
<!DOCTYPE html>
<html lang="de">
<head>
<meta charset="utf-8">
<title>Lenk &amp; Stabe Elektrotechnik – Fahne</title>
<link rel="stylesheet" href="https://fonts.googleapis.com/css2?family=Montserrat:wght@400;600&display=swap">
<style>
  :root {
    --brand-blue: #0087c8;
    --deep-blue: #034f8f;
    --paper: #ffffff;
    --text-light: #ffffff;
  }
  html, body {
    margin: 0;
    padding: 0;
    width: 1081px;
    height: 1200px;
    overflow: hidden;
    background: var(--paper);
  }
  .canvas {
    position: relative;
    width: 1081px;
    height: 1200px;
    background: var(--paper);
  }
  .flag {
    position: absolute;
    left: 349px;
    top: 108px;
    width: 382px;
    height: 1018px;
    background: var(--paper);
    box-shadow: 0 0 18px rgba(0, 0, 0, 0.12);
    overflow: hidden;
  }
  .flag__bands {
    position: absolute;
    inset: 0;
    width: 382px;
    height: 1018px;
  }
  .brand {
    position: absolute;
    left: 0;
    top: 128px;
    width: 382px;
    text-align: center;
    font-family: "Montserrat", sans-serif;
    font-weight: 600;
    color: var(--brand-blue);
  }
  .brand__mark {
    display: block;
    width: 88px;
    height: 88px;
    margin: 0 auto 38px;
    border: 4px solid var(--brand-blue);
    border-radius: 50%;
    box-sizing: border-box;
  }
  .brand__name {
    display: block;
    font-size: 33px;
    line-height: 1;
    letter-spacing: 0.5px;
  }
  .brand__trade {
    display: block;
    margin-top: 12px;
    font-size: 13px;
    letter-spacing: 4px;
  }
  .contacts {
    position: absolute;
    left: 0;
    top: 0;
    width: 382px;
    margin: 0;
    padding: 0;
    list-style: none;
    font-family: "Montserrat", sans-serif;
    font-weight: 400;
    font-size: 17px;
    color: var(--text-light);
  }
  .contact {
    position: absolute;
    left: 0;
    width: 382px;
    height: 34px;
  }
  .contact--web { top: 677px; }
  .contact--instagram { top: 745px; }
  .contact--facebook { top: 817px; }
  .contact__icon {
    position: absolute;
    left: 26px;
    top: 1px;
    width: 32px;
    height: 32px;
  }
  .contact__dot {
    position: absolute;
    left: 26px;
    top: 1px;
    width: 32px;
    height: 32px;
    border-radius: 50%;
    border: 2.5px solid var(--text-light);
    box-sizing: border-box;
  }
  .contact__text {
    position: absolute;
    left: 100px;
    top: 6px;
    line-height: 20px;
    white-space: nowrap;
  }
</style>
</head>
<body>
<div class="canvas">
  <section class="flag">
    <svg class="flag__bands" viewBox="0 0 382 1018" aria-hidden="true">
      <polygon points="0,462 382,368 382,382 0,478" fill="var(--brand-blue)"/>
      <polygon points="0,487 382,390 382,1018 0,1018" fill="var(--brand-blue)"/>
      <polygon points="0,487 82,466.3 82,1018 0,1018" fill="var(--deep-blue)"/>
    </svg>

    <header class="brand">
      <span class="brand__mark"></span>
      <span class="brand__name">LENK &amp; STABE</span>
      <span class="brand__trade">ELEKTROTECHNIK</span>
    </header>

    <ul class="contacts">
      <li class="contact contact--web">
        <svg class="contact__icon" viewBox="0 0 32 32" aria-hidden="true">
          <g fill="none" stroke="var(--text-light)" stroke-width="2.5">
            <circle cx="16" cy="16" r="13.5"/>
            <ellipse cx="16" cy="16" rx="5.5" ry="13.5"/>
            <line x1="2.5" y1="16" x2="29.5" y2="16"/>
          </g>
        </svg>
        <span class="contact__text">www.lenk-stabe.de</span>
      </li>
      <li class="contact contact--instagram">
        <span class="contact__dot"></span>
        <span class="contact__text">lenk_stabe_elektrotechnik</span>
      </li>
      <li class="contact contact--facebook">
        <span class="contact__dot"></span>
        <span class="contact__text">@lenkstabeelektrotechnik</span>
      </li>
    </ul>
  </section>
</div>
</body>
</html>
```